Business Cards for a small business advisory (business services)

Professional look. Same as would apply for a lawyer, accountant, or other financial services professional. Please use the logo colors

Target Market(s)

small business owners

Industry/Entity Type

Financial Servics

Contact Information for Business Card

Name: Gavin L. Whitmore, CAIA / Title: Business Advisor / Office #: (718) 294-7716 / Mobile #: (917) 382-5047 / Email: g.whitmore@clearfieldventurepartners.example / Web: www.clearfieldventurepartners.example

Font styles to use
Sans Serif

```html
<!DOCTYPE html>
<html lang="en">
<head>
<meta charset="utf-8">
<title>Clearfield Business Cards</title>
<link rel="stylesheet" href="https://fonts.googleapis.com/css2?family=Montserrat:wght@600;700&family=Roboto:wght@400;500;700&display=swap">
<style>
  :root {
    --navy: #263a6b;
    --navy-deep: #1f3160;
    --green: #8cc63f;
    --paper: #ffffff;
    --ink: #2a3d6e;
    --stage: #e6e7ea;
  }
  * { box-sizing: border-box; margin: 0; padding: 0; }
  html, body { width: 1200px; height: 852px; overflow: hidden; }
  body {
    background: var(--stage);
    font-family: "Roboto", Arial, sans-serif;
    position: relative;
  }
  .card {
    position: absolute;
    top: 276px;
    width: 525px;
    height: 300px;
    border-radius: 24px;
    overflow: hidden;
    box-shadow: 0 8px 24px rgba(0,0,0,0.18);
  }
  .card-back { left: 45px; background: var(--navy); }
  .card-front { left: 630px; background: var(--paper); }

  .back-edge {
    position: absolute; left: 0; right: 0; bottom: 0; height: 8px;
    background: var(--green);
  }
  .brand {
    position: absolute;
    display: flex; align-items: center; gap: 12px;
    font-family: "Montserrat", Arial, sans-serif;
    font-weight: 700;
    letter-spacing: -0.5px;
  }
  .brand-dot { border-radius: 50%; background: var(--green); flex: none; }
  .card-back .brand { left: 0; right: 0; top: 98px; justify-content: center; color: var(--paper); font-size: 58px; }
  .card-back .brand-dot { width: 44px; height: 44px; }

  .rule-top {
    position: absolute; right: 60px; top: 182px; width: 150px; height: 2px;
    background: linear-gradient(to right, rgba(255,255,255,0), #fff);
  }
  .slogan-row {
    position: absolute; left: 0; right: 0; top: 226px;
    display: flex; align-items: center; justify-content: center; gap: 12px;
    color: var(--paper); font-size: 15px;
  }
  .slogan-row .rule { width: 90px; height: 2px; background: linear-gradient(to right, rgba(255,255,255,0), #fff); }

  .card-front .brand { left: 30px; top: 28px; color: var(--ink); font-size: 46px; }
  .card-front .brand-dot { width: 36px; height: 36px; }

  .person { position: absolute; left: 32px; top: 126px; color: var(--ink); }
  .person-name { font-size: 21px; font-weight: 700; }
  .person-title { font-size: 15px; margin-top: 3px; }
  .person-rule { width: 120px; height: 2px; background: var(--green); margin-top: 6px; }

  .phones { position: absolute; left: 32px; top: 206px; color: var(--ink); font-size: 15px; line-height: 24px; }
  .contact-line { display: flex; align-items: center; gap: 8px; white-space: nowrap; }
  .contact-line svg { flex: none; }

  .email { position: absolute; right: 22px; top: 208px; color: var(--ink); font-size: 13px; }

  .front-bands { position: absolute; left: 0; bottom: 0; }
  .website {
    position: absolute; right: 20px; bottom: 22px;
    color: var(--navy-deep); font-size: 13px; font-weight: 500; white-space: nowrap;
  }
</style>
</head>
<body>
  <section class="card card-back" aria-label="Card back">
    <div class="brand"><span class="brand-dot"></span><span class="brand-name">Clearfield</span></div>
    <div class="rule-top"></div>
    <div class="slogan-row"><span class="rule"></span><span class="slogan">Be a vintage your house</span></div>
    <div class="back-edge"></div>
  </section>

  <section class="card card-front" aria-label="Card front">
    <div class="brand"><span class="brand-dot"></span><span class="brand-name">Clearfield</span></div>

    <div class="person">
      <div class="person-name">Gavin L. Whitmore, CAIA</div>
      <div class="person-title">Business Advisor</div>
      <div class="person-rule"></div>
    </div>

    <div class="phones">
      <div class="contact-line">
        <svg width="14" height="14" viewBox="0 0 24 24" aria-hidden="true"><path fill="#8cc63f" d="M6.6 10.8a15.1 15.1 0 0 0 6.6 6.6l2.2-2.2c.3-.3.7-.4 1-.2 1.1.4 2.3.6 3.6.6.6 0 1 .4 1 1V20c0 .6-.4 1-1 1A17 17 0 0 1 3 4c0-.6.4-1 1-1h3.5c.6 0 1 .4 1 1 0 1.3.2 2.5.6 3.6.1.3 0 .7-.2 1z"/></svg>
        <span>(718) 294-7716</span>
      </div>
      <div class="contact-line">
        <svg width="14" height="14" viewBox="0 0 24 24" aria-hidden="true"><path fill="#8cc63f" d="M6.6 10.8a15.1 15.1 0 0 0 6.6 6.6l2.2-2.2c.3-.3.7-.4 1-.2 1.1.4 2.3.6 3.6.6.6 0 1 .4 1 1V20c0 .6-.4 1-1 1A17 17 0 0 1 3 4c0-.6.4-1 1-1h3.5c.6 0 1 .4 1 1 0 1.3.2 2.5.6 3.6.1.3 0 .7-.2 1z"/></svg>
        <span>(917) 382-5047</span>
      </div>
    </div>

    <div class="email contact-line">
      <svg width="13" height="10" viewBox="0 0 26 20" aria-hidden="true"><rect width="26" height="20" rx="2" fill="#8cc63f"/><path d="M2 3l11 8 11-8" fill="none" stroke="#fff" stroke-width="2"/></svg>
      <span>g.whitmore@clearfieldventurepartners.example</span>
    </div>

    <svg class="front-bands" width="525" height="70" viewBox="0 0 525 70" aria-hidden="true">
      <polygon points="0,60 525,60 525,70 0,70" fill="#263a6b"/>
      <path d="M262,16 Q266,8 276,8 L525,8 L525,60 L250,60 Z" fill="#8cc63f"/>
    </svg>
    <div class="website">www.clearfieldventurepartners.example</div>
  </section>
</body>
</html>
```